TR Advisory Business Cards - High End AV / Low Voltage Company

We are low voltage AV company that specializes in high end clients on the residential side and larger businesses on the commercial side. We want something modern, tech looking but also something that is extremely professional looking. We have uploaded our logos and postcards we already have in the field. Along with a picture of one of our wrapped vans. Our website is at www.trvadvisory.example and our primary colors are the orange, green, grey and blue all military color finishes.

We are interesting in the slogans "Pairing You with the Right Technology" or "Leading the Lowcountry in Tech"

Target Market(s)

We focus on 70% Commercial and 30% Residential Customers

Industry/Entity Type

Low Voltage, AV Company

Contact Information for Business Card

Name - Dorian Fairweather, Title - Owner, Office Phone - 555-714-3096, Mobile Phone - 555-802-4173, E-Mail - d@trvadvisory.example, Website: www.trvadvisory.example

Font styles to use
Sans Serif

Requirements
Must have
• Must have Name, Title, Work Phone & Mobile, Website and Logo.
Nice to have
• We want something that will impress our higher end clients with a great logo
Should not have
• Too traditional or plain.

```html
<!DOCTYPE html>
<html lang="en">
<head>
<meta charset="utf-8">
<title>TR Advisory Business Cards</title>
<link rel="stylesheet" href="https://fonts.googleapis.com/css2?family=Montserrat:wght@500;600;700&family=Open+Sans:wght@400;600;700&display=swap">
<style>
  :root {
    --backdrop: #d3d4d6;
    --olive: #404620;
    --olive-deep: #252c14;
    --olive-text: #3a4220;
    --orange: #e8643a;
    --orange-title: #ec7d2e;
    --white: #ffffff;
  }
  html, body {
    margin: 0;
    padding: 0;
    width: 900px;
    height: 1200px;
    overflow: hidden;
    background: var(--backdrop);
  }
  .canvas {
    position: relative;
    width: 900px;
    height: 1200px;
  }
  .card {
    position: absolute;
    border-radius: 15px;
    overflow: hidden;
  }
  .card svg { display: block; width: 100%; height: 100%; }
  .card-front { left: 136px; top: 215px; width: 630px; height: 357px; background: var(--olive); }
  .card-back { left: 135px; top: 628px; width: 632px; height: 359px; background: var(--white); }
  .service-label {
    font-family: "Montserrat", sans-serif;
    font-weight: 600;
    font-size: 20px;
    letter-spacing: 0.5px;
    fill: var(--white);
  }
  .circuit { fill: none; stroke: var(--white); stroke-width: 3; }
  .node { fill: var(--orange); }
  .brand-name {
    font-family: "Montserrat", sans-serif;
    font-weight: 700;
    fill: var(--orange);
  }
  .person-name {
    font-family: "Open Sans", sans-serif;
    font-weight: 700;
    font-size: 34px;
    fill: var(--olive-text);
  }
  .person-title {
    font-family: "Open Sans", sans-serif;
    font-weight: 600;
    font-size: 24px;
    letter-spacing: 1px;
    fill: var(--orange-title);
  }
  .contact {
    font-family: "Open Sans", sans-serif;
    font-weight: 400;
    font-size: 24px;
    fill: var(--olive-text);
  }
  .contact-phone { letter-spacing: 3px; }
  .contact-web { letter-spacing: 0.8px; }
  .icon { fill: var(--orange); }
  .icon-line { fill: none; stroke: var(--orange); stroke-width: 2; }
  .tagline {
    font-family: "Montserrat", sans-serif;
    font-weight: 600;
    font-size: 22px;
    fill: var(--white);
  }
</style>
</head>
<body>
<main class="canvas">

  <section class="card card-front" aria-label="Business card front">
    <svg viewBox="0 0 840 476" xmlns="http://www.w3.org/2000/svg">
      <g class="services">
        <polyline class="circuit" points="222,83 222,155 246,180"/>
        <circle class="node" cx="222" cy="83" r="6"/>
        <text class="service-label" x="149" y="69">MANAGED I.T.</text>

        <polyline class="circuit" points="692,123 692,173 651,213 601,213"/>
        <circle class="node" cx="692" cy="123" r="6"/>
        <text class="service-label" x="617" y="109">SMART HOME</text>

        <polyline class="circuit" points="603,250 659,250 684,275 684,343"/>
        <circle class="node" cx="684" cy="343" r="6"/>
        <text class="service-label" x="629" y="367">SECURITY</text>

        <polyline class="circuit" points="140,401 140,388 165,362 223,362 240,378 302,378"/>
        <circle class="node" cx="140" cy="401" r="6"/>
        <text class="service-label" x="40" y="431">STRUCTURED WIRING</text>
      </g>
      <circle cx="419" cy="238" r="183" fill="var(--olive-deep)"/>
      <text class="brand-name" x="419" y="256" font-size="50" text-anchor="middle">TR Advisory</text>
    </svg>
  </section>

  <section class="card card-back" aria-label="Business card back">
    <svg viewBox="0 0 842 478" xmlns="http://www.w3.org/2000/svg">
      <text class="brand-name" x="245" y="268" font-size="44" text-anchor="middle">TR Advisory</text>

      <rect x="420" y="118" width="3" height="242" fill="var(--olive-text)"/>

      <text class="person-name" x="469" y="160">Dorian Fairweather</text>
      <text class="person-title" x="469" y="190">Owner</text>

      <g class="contact-list">
        <path class="icon" d="M470 232 q2 -4 5 -2 l3 4 q1 2 -1 3 q2 5 6 7 q1 -2 3 -1 l4 3 q2 3 -2 5 q-8 2 -14 -6 q-6 -7 -4 -13z"/>
        <text class="contact contact-phone" x="495" y="241">555-714-3096</text>

        <rect class="icon" x="470" y="257" width="14" height="23" rx="2"/>
        <rect x="473" y="261" width="8" height="13" fill="var(--white)"/>
        <text class="contact contact-phone" x="495" y="275">555-802-4173</text>

        <rect class="icon" x="468" y="297" width="18" height="12"/>
        <polyline points="468,297 477,304 486,297" fill="none" stroke="var(--white)" stroke-width="1.5"/>
        <text class="contact" x="495" y="309">d@trvadvisory.example</text>

        <circle class="icon-line" cx="477" cy="336" r="8"/>
        <line class="icon-line" x1="469" y1="336" x2="485" y2="336"/>
        <ellipse class="icon-line" cx="477" cy="336" rx="3.5" ry="8"/>
        <text class="contact contact-web" x="495" y="344">www.trvadvisory.example</text>
      </g>

      <rect x="0" y="390" width="842" height="62" fill="var(--olive)"/>
      <line x1="50" y1="421" x2="132" y2="421" stroke="var(--white)" stroke-width="2.5"/>
      <circle class="node" cx="50" cy="421" r="6"/>
      <line x1="710" y1="421" x2="792" y2="421" stroke="var(--white)" stroke-width="2.5"/>
      <circle class="node" cx="792" cy="421" r="6"/>
      <text class="tagline" x="421" y="429" text-anchor="middle">PAIRING YOU WITH THE RIGHT TECHNOLOGY</text>
    </svg>
  </section>

</main>
</body>
</html>
```